Business card design needed

I have started a new business called Marlow Auto Electrical, although the words Marlow Auto Electrical will be used on signage and documents I actually want to market the business as MAE. The services I offer are Mobile Auto Electrical, Automotive Air Conditioning and Test And Tag. My business will be targetting the Mining Industry, Civil, Rail, Agricultural and Workshop Testing And Tagging. My auto electrical service ranges from fault finding to new vehicle and mine compliance fit outs. I have a very strong focus on quality workmanship. I will upload the logo I have designed and want to use I am happy for the logo colour to change but the design itself must stay the same. I want the design to have a modern, eye catching, energetic feel. As I am a passionate motorsport fan I am happy for this to also influence the design. I am happy for the front of the card to have only the emblem and logo design and the back to have all the info.

Industry/Entity Type

Electrical

Contact Information for Business Card

MAE Marlow Auto Electrical, Dale Penrick, Auto Electrician, Mobile No 0417263859

Requirements
Must have
• On the business card it is mandatory that the following license numbers are shown:

MVRL38462
VDA L071348
ABN 61 839 204 518

```html
<!DOCTYPE html>
<html lang="en">
<head>
<meta charset="utf-8">
<title>Marlow Auto Electrical – Business Card</title>
<link rel="stylesheet" href="https://fonts.googleapis.com/css2?family=Michroma&display=swap">
<style>
  :root {
    --page-bg: #ffffff;
    --card-black: #070707;
    --card-glow: #4a4a4a;
    --card-mid: #1c1c1c;
    --ink-white: #ffffff;
    --ink-soft: #e6e6e6;
  }
  html, body {
    margin: 0;
    padding: 0;
    width: 1200px;
    height: 741px;
    overflow: hidden;
    background: var(--page-bg);
  }
  .canvas {
    position: relative;
    width: 1200px;
    height: 741px;
    display: flex;
    align-items: center;
    justify-content: center;
    gap: 40px;
  }
  .card {
    position: relative;
    width: 540px;
    height: 309px;
    background: var(--card-black);
    overflow: hidden;
    box-shadow: 0 6px 18px rgba(0,0,0,0.18);
  }
  .card__texture {
    position: absolute;
    inset: 0;
    background: radial-gradient(ellipse 70% 80% at 40% 45%, var(--card-glow) 0%, var(--card-mid) 45%, var(--card-black) 85%);
  }
  .card--front .card__texture {
    background: radial-gradient(ellipse 65% 75% at 45% 55%, var(--card-glow) 0%, var(--card-mid) 48%, var(--card-black) 88%);
  }
  .brand-name {
    position: absolute;
    margin: 0;
    font-family: "Michroma", sans-serif;
    font-weight: 400;
    color: var(--ink-white);
    text-transform: uppercase;
    white-space: nowrap;
    line-height: 1.2;
  }
  .card--front .brand-name {
    left: 50%;
    top: 50%;
    transform: translate(-50%, -50%);
    font-size: 22px;
    letter-spacing: 0.02em;
  }
  .card--back .brand-name {
    right: 30px;
    top: 56px;
    font-size: 14px;
    letter-spacing: 0.02em;
  }
  .contact {
    position: absolute;
    right: 30px;
    top: 150px;
    text-align: right;
    font-family: "Michroma", sans-serif;
    color: var(--ink-soft);
    text-transform: uppercase;
  }
  .contact__name {
    font-size: 15px;
    color: var(--ink-white);
    margin: 0 0 2px;
    letter-spacing: 0.02em;
  }
  .contact__line {
    font-size: 10.5px;
    margin: 0;
    line-height: 1.45;
  }
  .contact__licences {
    margin-top: 16px;
  }
</style>
</head>
<body>
<main class="canvas">
  <section class="card card--front" aria-label="Card front">
    <div class="card__texture" role="img" aria-label="Dark perforated metal texture with a soft central highlight"></div>
    <p class="brand-name">Marlow Auto Electrical</p>
  </section>

  <section class="card card--back" aria-label="Card back">
    <div class="card__texture" role="img" aria-label="Dark perforated metal texture with a soft highlight on the left"></div>
    <p class="brand-name">Marlow Auto Electrical</p>
    <div class="contact">
      <p class="contact__name">Dale Penrick</p>
      <p class="contact__line">Auto Electrician</p>
      <p class="contact__line">Ph: 0417263859</p>
      <div class="contact__licences">
        <p class="contact__line">MVRL38462</p>
        <p class="contact__line">VDA L071348</p>
        <p class="contact__line">ABN 61 839 204 518</p>
      </div>
    </div>
  </section>
</main>
</body>
</html>
```